Design the Mobile Version of Existing Web Based Health Platform

Loomcrest is a social business enterprise that focus on public health by applying innovative healthcare services and consumer internet technology. Loomcrest offers a personalized platform of health promotion and disease prevention that puts the individual back in control of his life.

Loomcrest is looking for a Mobile Web UX/Visual Design professional to create a mobile version of Loomcrest website platform for iPhone, iPad/tablet and Android.

Contestants must to check www.loomcrest-demo.com.br to have a better understanding of Loomcrest Platform by creating an account (it's in portuguese, but anyone can get the general idea).

The mobile version of Loomcrest should have very similar functionality and user flows. This job is not to reengineer or re-imagine Loomcrest. It is just to reformat the existing functionality so it works well on mobile devices.

This description below is to help you to understand the core features of the platform (check the attachments to see the new web design of each one):

- Personally Controlled Health Record - PCHR enables an individual to own and manage a complete, secure, digital copy of her health and wellness information.
- Health Risk Assessments - is a process to estimate the nature and probability of adverse health effects, based on personal and family historical data, behavior and environment.
- Simulation of future health - "what if analysis" that emphasizes health education and behavior change.
- Step Quests - a program that gives you the opportunity to the participant to advance his personal well-being by doing simple Step Quests
- Health Alerts and Recommendations and Missing Data - Recommendations based on Wellbeing Bureau Guidelines and Federal Wellness Review Panel (FWRP), plus notifications to update outdated information.

The deliverable for this project is a psd file with a designed mobile version of Loomcrest.

A new design of the web platform is under construction. You can also check it looking at the files attached.

Target Market(s)

people 25-40 years old, 60% female, socially engaged

Industry/Entity Type

Healthcare

Requirements
Must have
• iPhone, iPad and Android version

Design must cover all current functionalities available on the web version (please, ensure you understand all features by creating an account at www.loomcrest-demo.com.br)

- Login/Sign up
- Welcome (first assessment)
- Add to Personal Controlled Health Record (PCHR)
- Update/Remove PCHR
- List PCHR
- Riskgrid (risk assessmen results)
- Simulation
- Alerts
- Missing data
- Recommendations
- StepQuest
- Badges
- Configurations

It's important to check the attachments to see how the web platform design is evolving.

```html
<!DOCTYPE html>
<html lang="pt">
<head>
<meta charset="utf-8">
<title>Loomcrest Mobile – Assessment Flow</title>
<link href="https://fonts.googleapis.com/css2?family=Open+Sans:ital,wght@0,400;0,600;0,700;1,700&display=swap" rel="stylesheet">
<style>
:root{
  --stage:#e9e9e9;
  --screen-bg:#efefeb;
  --card:#ffffff;
  --bar:#eceeef;
  --line:#dcdcdc;
  --orange:#f7923a;
  --green:#8dc63f;
  --green-tile:#3fc46b;
  --tile:#a9abad;
  --tile-edge:#999b9d;
  --text:#7b7d80;
  --text-dark:#555;
  --alert:#e53935;
}
*{box-sizing:border-box;margin:0;padding:0}
html,body{width:1200px;height:800px;overflow:hidden;background:var(--stage);font-family:"Open Sans",Arial,sans-serif;color:var(--text)}
.screen{position:absolute;top:125px;width:305px;height:535px;background:var(--screen-bg);overflow:hidden}
.screen--one{left:70px}.screen--two{left:445px}.screen--three{left:820px}
.screen-backdrop{position:absolute;inset:0;background:linear-gradient(160deg,#f3f2ee,#e8e9e3)}
.card{position:absolute;left:22px;top:38px;width:258px;height:462px;background:var(--card);border-radius:3px;box-shadow:0 0 3px rgba(0,0,0,.08)}
.topbar{position:absolute;left:0;top:0;width:100%;height:30px;background:var(--bar);border-radius:3px 3px 0 0;font-size:6px}
.topbar .link{position:absolute;top:12px;color:var(--orange)}
.topbar .sep{position:absolute;top:10px;left:45px;width:1px;height:10px;background:#ccc}
.search{position:absolute;left:66px;top:8px;width:188px;height:14px;background:#fff;border:1px solid #ccc;border-radius:2px}
.search svg{position:absolute;right:3px;top:2px}
.avatar-block{position:absolute;left:3px;top:33px;width:63px;height:58px;background:var(--orange)}
.greeting{position:absolute;left:70px;top:42px;font-size:8.5px;font-weight:700;font-style:italic;color:var(--green)}
.toolbar{position:absolute;left:155px;top:37px;display:flex;gap:4px;align-items:center}
.toolbar .tool{width:19px;height:19px;border-left:1px solid #ddd;display:flex;align-items:center;justify-content:center;position:relative}
.badge{position:absolute;right:0;bottom:0;width:7px;height:7px;border-radius:50%;background:var(--orange);color:#fff;font-size:4px;text-align:center;line-height:7px}
.record{position:absolute;left:68px;top:71px}
.record-input{position:absolute;left:16px;top:0;width:168px;height:14px;border:1px solid #ccc;font-size:5.5px;color:#aaa;padding:3px 5px}
.divider{position:absolute;left:5px;width:248px;height:1px;background:var(--line)}
.nav{position:absolute;left:5px;top:103px;width:248px;display:grid;grid-template-columns:repeat(3,1fr);row-gap:6px}
.nav-item{display:flex;align-items:center;gap:6px;font-size:6.5px;padding-left:8px;height:19px;border-left:1px solid #eee}
.nav-item:nth-child(3n+1){border-left:none}
.nav-item .plus{width:13px;height:13px;background:var(--green);color:#fff;font-size:11px;line-height:12px;text-align:center;font-weight:700;margin-left:2px}
.menu{position:absolute;left:20px;top:171px;width:70px;display:flex;flex-direction:column;gap:2px}
.tile{height:28px;background:var(--tile);border:1px solid var(--tile-edge);display:flex;flex-direction:column;align-items:center;justify-content:flex-end;padding-bottom:2px;color:#fff;font-size:5.5px;text-shadow:0 0 1px rgba(0,0,0,.3)}
.tile svg{margin-bottom:2px}
.tile--active{background:var(--orange);border-color:#e07d27}
.tile--done{background:var(--green-tile);border-color:#31a85a}
.actions{position:absolute;left:60px;top:435px;display:flex;gap:5px}
.btn{width:62px;height:15px;background:var(--orange);color:#fff;font-size:6.5px;font-weight:600;text-align:center;line-height:15px}
.form{position:absolute;left:100px;font-size:6.5px}
.form .heading{color:var(--text-dark)}
.form .label{color:var(--orange);font-weight:600;margin-top:8px}
.field{margin-top:4px;width:85px;height:14px;border:1px solid #ccc;font-size:6px;text-align:right;padding:3px 5px;color:#666}
.field--error{border-color:var(--alert)}
.select{margin-top:4px;width:128px;height:14px;border:1px solid #ccc;font-size:6px;padding:3px 5px;position:relative;color:#666}
.select::after{content:"";position:absolute;right:5px;top:4px;border:4px solid transparent;border-top:5px solid #888}
.segment{display:flex;margin-top:5px}
.segment span{height:13px;border:1px solid #ccc;text-align:center;line-height:11px;font-size:5.5px;color:#777;margin-left:-1px}
.segment .on{background:var(--green-tile);color:#fff;border-color:var(--green-tile)}
.segment--error{border:1px solid var(--alert)}
.segment--error span{border:none;margin:0}
.hint{color:var(--alert);font-size:4.5px;display:flex;align-items:center;gap:3px;justify-content:flex-end;margin-top:3px}
</style>
</head>
<body>

<!-- ===== Screen 1 : empty assessment ===== -->
<section class="screen screen--one">
  <div class="screen-backdrop" role="img" aria-label="Faint pattern of fruit, bicycles and fitness items"></div>
  <div class="card">
    <header class="topbar">
      <span class="link" style="left:5px">Consultations</span><span class="sep"></span><span class="link" style="left:49px">Help</span>
      <div class="search"><svg width="8" height="8" viewBox="0 0 8 8"><circle cx="3.2" cy="3.2" r="2.4" fill="none" stroke="#888"/><path d="M5 5l2.5 2.5" stroke="#888"/></svg></div>
    </header>
    <div class="avatar-block"></div>
    <p class="greeting">Good day, Tavoreni!</p>
    <div class="toolbar">
      <div class="tool"><svg width="12" height="12"><g fill="#888"><rect x="0" y="0" width="3" height="3"/><rect x="4.5" y="0" width="3" height="3"/><rect x="9" y="0" width="3" height="3"/><rect x="0" y="4.5" width="3" height="3"/><rect x="4.5" y="4.5" width="3" height="3"/><rect x="9" y="4.5" width="3" height="3"/><rect x="0" y="9" width="3" height="3"/><rect x="4.5" y="9" width="3" height="3"/><rect x="9" y="9" width="3" height="3"/></g></svg></div>
      <div class="tool"><svg width="13" height="12"><path d="M6.5 0L13 12H0z" fill="#999"/><rect x="6" y="4" width="1" height="4" fill="#fff"/></svg><span class="badge">15</span></div>
      <div class="tool"><svg width="12" height="12"><rect x="1" y="1" width="10" height="10" fill="#999"/><path d="M3 4h6M3 6h6M3 8h4" stroke="#fff"/></svg></div>
      <div class="tool"><svg width="14" height="14"><rect width="14" height="14" fill="#ddd"/><circle cx="7" cy="5" r="3" fill="#999"/><path d="M1 14c0-4 12-4 12 0z" fill="#999"/></svg></div>
      <svg width="6" height="4"><path d="M0 0l3 3 3-3" stroke="#999" fill="none"/></svg>
    </div>
    <div class="record"><svg width="11" height="14"><rect x="0" y="1" width="11" height="13" fill="#8dc63f"/><path d="M2 5h7M2 8h7M2 11h7" stroke="#fff"/></svg><div class="record-input">Add a new record</div></div>
    <div class="divider" style="top:98px"></div>
    <nav class="nav">
      <div class="nav-item"><svg width="10" height="14"><circle cx="5" cy="3" r="3" fill="#f7923a"/><rect x="1" y="6" width="8" height="8" rx="2" fill="#f7923a"/></svg>Health Map</div>
      <div class="nav-item"><svg width="12" height="14"><circle cx="5" cy="3" r="3" fill="#f7923a"/><rect x="1" y="6" width="8" height="8" rx="2" fill="#f7923a"/><circle cx="10" cy="10" r="2" fill="#8dc63f"/></svg>Simulation</div>
      <div class="nav-item"><svg width="14" height="12"><rect x="0" y="0" width="10" height="8" rx="3" fill="none" stroke="#f7923a"/><rect x="4" y="4" width="10" height="8" rx="3" fill="none" stroke="#8dc63f"/></svg>Challenges</div>
      <div class="nav-item"><svg width="10" height="13"><rect width="10" height="13" fill="#f7923a"/><path d="M2 3h6M2 6h6" stroke="#fff"/></svg>Booklet<span class="plus">+</span></div>
      <div class="nav-item"><svg width="12" height="12"><path d="M2 0h8v5a4 4 0 0 1-8 0z" fill="#f7923a"/><rect x="4" y="9" width="4" height="3" fill="#8dc63f"/></svg>Trophies</div>
      <div class="nav-item"><svg width="11" height="11"><g fill="#f7923a"><rect width="3" height="3"/><rect x="4" width="3" height="3"/><rect x="8" width="3" height="3"/><rect y="4" width="3" height="3"/><rect x="4" y="4" width="3" height="3"/><rect x="8" y="4" width="3" height="3"/><rect y="8" width="3" height="3"/><rect x="4" y="8" width="3" height="3"/><rect x="8" y="8" width="3" height="3"/></g></svg>More</div>
    </nav>
    <div class="divider" style="top:155px"></div>
    <div class="menu">
      <div class="tile"><svg width="12" height="10"><rect x="1" y="1" width="10" height="8" rx="4" fill="none" stroke="#fff"/></svg>Dados e medidas</div>
      <div class="tile"><svg width="12" height="10"><path d="M2 9V4l4-3 3 3h2" stroke="#fff" fill="none"/></svg>Atividade física</div>
      <div class="tile"><svg width="14" height="8"><rect x="1" y="4" width="12" height="3" fill="#fff"/><path d="M11 1v2" stroke="#fff"/></svg>Consumo de cigarro</div>
      <div class="tile"><svg width="12" height="10"><rect x="2" y="2" width="8" height="6" rx="3" fill="#fff" transform="rotate(-35 6 5)"/></svg>Informações clínicas</div>
      <div class="tile"><svg width="14" height="10"><circle cx="4" cy="3" r="2" fill="#fff"/><circle cx="10" cy="3" r="2" fill="#fff"/><path d="M1 10c0-4 6-4 6 0M7 10c0-4 6-4 6 0" fill="#fff"/></svg>Histórico familiar</div>
      <div class="tile"><svg width="10" height="12"><circle cx="5" cy="4" r="3" fill="none" stroke="#fff" stroke-width="1.5"/><path d="M5 7v5M3 10h4" stroke="#fff" stroke-width="1.5"/></svg>Saúde da mulher</div>
      <div class="tile"><svg width="12" height="10"><path d="M1 0v9h11M2 7l3-3 2 2 4-5" stroke="#fff" fill="none"/></svg>Histórico pessoal</div>
      <div class="tile"><svg width="12" height="10"><rect x="1" y="3" width="10" height="4" rx="2" fill="#fff" transform="rotate(-30 6 5)"/></svg>Remédios</div>
    </div>
    <div class="actions"><span class="btn">Back</span><span class="btn">Next</span></div>
  </div>
</section>

<!-- ===== Screen 2 : measurements ===== -->
<section class="screen screen--two">
  <div class="screen-backdrop" role="img" aria-label="Faint pattern of fruit, bicycles and fitness items"></div>
  <div class="card">
    <header class="topbar">
      <span class="link" style="left:5px">Consultations</span><span class="sep"></span><span class="link" style="left:49px">Help</span>
      <div class="search"><svg width="8" height="8" viewBox="0 0 8 8"><circle cx="3.2" cy="3.2" r="2.4" fill="none" stroke="#888"/><path d="M5 5l2.5 2.5" stroke="#888"/></svg></div>
    </header>
    <div class="avatar-block"></div>
    <p class="greeting">Good day, Tavoreni!</p>
    <div class="toolbar">
      <div class="tool"><svg width="12" height="12"><g fill="#888"><rect x="0" y="0" width="3" height="3"/><rect x="4.5" y="0" width="3" height="3"/><rect x="9" y="0" width="3" height="3"/><rect x="0" y="4.5" width="3" height="3"/><rect x="4.5" y="4.5" width="3" height="3"/><rect x="9" y="4.5" width="3" height="3"/><rect x="0" y="9" width="3" height="3"/><rect x="4.5" y="9" width="3" height="3"/><rect x="9" y="9" width="3" height="3"/></g></svg></div>
      <div class="tool"><svg width="13" height="12"><path d="M6.5 0L13 12H0z" fill="#999"/><rect x="6" y="4" width="1" height="4" fill="#fff"/></svg><span class="badge">15</span></div>
      <div class="tool"><svg width="12" height="12"><rect x="1" y="1" width="10" height="10" fill="#999"/><path d="M3 4h6M3 6h6M3 8h4" stroke="#fff"/></svg></div>
      <div class="tool"><svg width="14" height="14"><rect width="14" height="14" fill="#ddd"/><circle cx="7" cy="5" r="3" fill="#999"/><path d="M1 14c0-4 12-4 12 0z" fill="#999"/></svg></div>
      <svg width="6" height="4"><path d="M0 0l3 3 3-3" stroke="#999" fill="none"/></svg>
    </div>
    <div class="record"><svg width="11" height="14"><rect x="0" y="1" width="11" height="13" fill="#8dc63f"/><path d="M2 5h7M2 8h7M2 11h7" stroke="#fff"/></svg><div class="record-input">Add a new record</div></div>
    <div class="divider" style="top:98px"></div>
    <nav class="nav">
      <div class="nav-item"><svg width="10" height="14"><circle cx="5" cy="3" r="3" fill="#f7923a"/><rect x="1" y="6" width="8" height="8" rx="2" fill="#f7923a"/></svg>Health Map</div>
      <div class="nav-item"><svg width="12" height="14"><circle cx="5" cy="3" r="3" fill="#f7923a"/><rect x="1" y="6" width="8" height="8" rx="2" fill="#f7923a"/><circle cx="10" cy="10" r="2" fill="#8dc63f"/></svg>Simulation</div>
      <div class="nav-item"><svg width="14" height="12"><rect x="0" y="0" width="10" height="8" rx="3" fill="none" stroke="#f7923a"/><rect x="4" y="4" width="10" height="8" rx="3" fill="none" stroke="#8dc63f"/></svg>Challenges</div>
      <div class="nav-item"><svg width="10" height="13"><rect width="10" height="13" fill="#f7923a"/><path d="M2 3h6M2 6h6" stroke="#fff"/></svg>Booklet<span class="plus">+</span></div>
      <div class="nav-item"><svg width="12" height="12"><path d="M2 0h8v5a4 4 0 0 1-8 0z" fill="#f7923a"/><rect x="4" y="9" width="4" height="3" fill="#8dc63f"/></svg>Trophies</div>
      <div class="nav-item"><svg width="11" height="11"><g fill="#f7923a"><rect width="3" height="3"/><rect x="4" width="3" height="3"/><rect x="8" width="3" height="3"/><rect y="4" width="3" height="3"/><rect x="4" y="4" width="3" height="3"/><rect x="8" y="4" width="3" height="3"/><rect y="8" width="3" height="3"/><rect x="4" y="8" width="3" height="3"/><rect x="8" y="8" width="3" height="3"/></g></svg>More</div>
    </nav>
    <div class="divider" style="top:155px"></div>
    <div class="menu">
      <div class="tile tile--active"><svg width="12" height="10"><rect x="1" y="1" width="10" height="8" rx="4" fill="none" stroke="#fff"/></svg>Dados e medidas</div>
      <div class="tile"><svg width="12" height="10"><path d="M2 9V4l4-3 3 3h2" stroke="#fff" fill="none"/></svg>Atividade física</div>
      <div class="tile"><svg width="14" height="8"><rect x="1" y="4" width="12" height="3" fill="#fff"/><path d="M11 1v2" stroke="#fff"/></svg>Consumo de cigarro</div>
      <div class="tile"><svg width="12" height="10"><rect x="2" y="2" width="8" height="6" rx="3" fill="#fff" transform="rotate(-35 6 5)"/></svg>Informações clínicas</div>
      <div class="tile"><svg width="14" height="10"><circle cx="4" cy="3" r="2" fill="#fff"/><circle cx="10" cy="3" r="2" fill="#fff"/><path d="M1 10c0-4 6-4 6 0M7 10c0-4 6-4 6 0" fill="#fff"/></svg>Histórico familiar</div>
      <div class="tile"><svg width="10" height="12"><circle cx="5" cy="4" r="3" fill="none" stroke="#fff" stroke-width="1.5"/><path d="M5 7v5M3 10h4" stroke="#fff" stroke-width="1.5"/></svg>Saúde da mulher</div>
      <div class="tile"><svg width="12" height="10"><path d="M1 0v9h11M2 7l3-3 2 2 4-5" stroke="#fff" fill="none"/></svg>Histórico pessoal</div>
      <div class="tile"><svg width="12" height="10"><rect x="1" y="3" width="10" height="4" rx="2" fill="#fff" transform="rotate(-30 6 5)"/></svg>Remédios</div>
    </div>
    <form class="form" style="top:240px">
      <p class="heading">Minhas medidas:</p>
      <p class="label">Peso atual</p>
      <div class="field">60 &nbsp;&nbsp;&nbsp;&nbsp;&nbsp; Kg</div>
      <p class="label">Altura atual</p>
      <div style="display:flex;align-items:center;gap:6px"><div class="field field--error">cm</div><svg width="9" height="8" style="margin-top:4px"><path d="M4.5 0L9 8H0z" fill="#e53935"/><rect x="4" y="2.5" width="1" height="3" fill="#fff"/></svg></div>
      <p class="label">Circunferência da cintura atual</p>
      <div class="select">Media</div>
    </form>
    <div class="actions"><span class="btn">Back</span><span class="btn">Next</span></div>
  </div>
</section>

<!-- ===== Screen 3 : physical activity ===== -->
<section class="screen screen--three">
  <div class="screen-backdrop" role="img" aria-label="Faint pattern of fruit, bicycles and fitness items"></div>
  <div class="card">
    <header class="topbar">
      <span class="link" style="left:5px">Consultations</span><span class="sep"></span><span class="link" style="left:49px">Help</span>
      <div class="search"><svg width="8" height="8" viewBox="0 0 8 8"><circle cx="3.2" cy="3.2" r="2.4" fill="none" stroke="#888"/><path d="M5 5l2.5 2.5" stroke="#888"/></svg></div>
    </header>
    <div class="avatar-block"></div>
    <p class="greeting">Good day, Tavoreni!</p>
    <div class="toolbar">
      <div class="tool"><svg width="12" height="12"><g fill="#888"><rect x="0" y="0" width="3" height="3"/><rect x="4.5" y="0" width="3" height="3"/><rect x="9" y="0" width="3" height="3"/><rect x="0" y="4.5" width="3" height="3"/><rect x="4.5" y="4.5" width="3" height="3"/><rect x="9" y="4.5" width="3" height="3"/><rect x="0" y="9" width="3" height="3"/><rect x="4.5" y="9" width="3" height="3"/><rect x="9" y="9" width="3" height="3"/></g></svg></div>
      <div class="tool"><svg width="13" height="12"><path d="M6.5 0L13 12H0z" fill="#999"/><rect x="6" y="4" width="1" height="4" fill="#fff"/></svg><span class="badge">15</span></div>
      <div class="tool"><svg width="12" height="12"><rect x="1" y="1" width="10" height="10" fill="#999"/><path d="M3 4h6M3 6h6M3 8h4" stroke="#fff"/></svg></div>
      <div class="tool"><svg width="14" height="14"><rect width="14" height="14" fill="#ddd"/><circle cx="7" cy="5" r="3" fill="#999"/><path d="M1 14c0-4 12-4 12 0z" fill="#999"/></svg></div>
      <svg width="6" height="4"><path d="M0 0l3 3 3-3" stroke="#999" fill="none"/></svg>
    </div>
    <div class="record"><svg width="11" height="14"><rect x="0" y="1" width="11" height="13" fill="#8dc63f"/><path d="M2 5h7M2 8h7M2 11h7" stroke="#fff"/></svg><div class="record-input">Add a new record</div></div>
    <div class="divider" style="top:98px"></div>
    <nav class="nav">
      <div class="nav-item"><svg width="10" height="14"><circle cx="5" cy="3" r="3" fill="#f7923a"/><rect x="1" y="6" width="8" height="8" rx="2" fill="#f7923a"/></svg>Health Map</div>
      <div class="nav-item"><svg width="12" height="14"><circle cx="5" cy="3" r="3" fill="#f7923a"/><rect x="1" y="6" width="8" height="8" rx="2" fill="#f7923a"/><circle cx="10" cy="10" r="2" fill="#8dc63f"/></svg>Simulation</div>
      <div class="nav-item"><svg width="14" height="12"><rect x="0" y="0" width="10" height="8" rx="3" fill="none" stroke="#f7923a"/><rect x="4" y="4" width="10" height="8" rx="3" fill="none" stroke="#8dc63f"/></svg>Challenges</div>
      <div class="nav-item"><svg width="10" height="13"><rect width="10" height="13" fill="#f7923a"/><path d="M2 3h6M2 6h6" stroke="#fff"/></svg>Booklet<span class="plus">+</span></div>
      <div class="nav-item"><svg width="12" height="12"><path d="M2 0h8v5a4 4 0 0 1-8 0z" fill="#f7923a"/><rect x="4" y="9" width="4" height="3" fill="#8dc63f"/></svg>Trophies</div>
      <div class="nav-item"><svg width="11" height="11"><g fill="#f7923a"><rect width="3" height="3"/><rect x="4" width="3" height="3"/><rect x="8" width="3" height="3"/><rect y="4" width="3" height="3"/><rect x="4" y="4" width="3" height="3"/><rect x="8" y="4" width="3" height="3"/><rect y="8" width="3" height="3"/><rect x="4" y="8" width="3" height="3"/><rect x="8" y="8" width="3" height="3"/></g></svg>More</div>
    </nav>
    <div class="divider" style="top:155px"></div>
    <div class="menu">
      <div class="tile tile--done"><svg width="12" height="10"><rect x="1" y="1" width="10" height="8" rx="4" fill="none" stroke="#fff"/></svg>Dados e medidas</div>
      <div class="tile tile--active"><svg width="12" height="10"><path d="M2 9V4l4-3 3 3h2" stroke="#fff" fill="none"/></svg>Atividade física</div>
      <div class="tile"><svg width="14" height="8"><rect x="1" y="4" width="12" height="3" fill="#fff"/><path d="M11 1v2" stroke="#fff"/></svg>Consumo de cigarro</div>
      <div class="tile"><svg width="12" height="10"><rect x="2" y="2" width="8" height="6" rx="3" fill="#fff" transform="rotate(-35 6 5)"/></svg>Informações clínicas</div>
      <div class="tile"><svg width="14" height="10"><circle cx="4" cy="3" r="2" fill="#fff"/><circle cx="10" cy="3" r="2" fill="#fff"/><path d="M1 10c0-4 6-4 6 0M7 10c0-4 6-4 6 0" fill="#fff"/></svg>Histórico familiar</div>
      <div class="tile"><svg width="10" height="12"><circle cx="5" cy="4" r="3" fill="none" stroke="#fff" stroke-width="1.5"/><path d="M5 7v5M3 10h4" stroke="#fff" stroke-width="1.5"/></svg>Saúde da mulher</div>
      <div class="tile"><svg width="12" height="10"><path d="M1 0v9h11M2 7l3-3 2 2 4-5" stroke="#fff" fill="none"/></svg>Histórico pessoal</div>
      <div class="tile"><svg width="12" height="10"><rect x="1" y="3" width="10" height="4" rx="2" fill="#fff" transform="rotate(-30 6 5)"/></svg>Remédios</div>
    </div>
    <form class="form" style="top:222px;left:92px;width:130px">
      <p class="heading">Meu nível de atividade física</p>
      <p class="label" style="margin-top:10px">Quantas vezes por semana eu faço alguma atividade física (pelo menos 20 minutos)?</p>
      <div class="segment" style="margin-top:8px"><span style="width:35px">Never</span><span style="width:50px">1</span></div>
      <div class="segment" style="margin-top:8px"><span class="on" style="width:35px">2 - 4</span><span style="width:50px">More 5</span></div>
      <p class="heading" style="margin-top:14px">Quando me exercito,<br>minha respiração fica:</p>
      <div class="segment segment--error"><span style="width:42px">Normal</span><span style="width:42px">Medium</span><span style="width:42px">Intense</span></div>
      <p class="hint"><svg width="7" height="6"><path d="M3.5 0L7 6H0z" fill="#e53935"/></svg>Escolha uma opção!</p>
    </form>
    <div class="actions"><span class="btn">Back</span><span class="btn">Next</span></div>
  </div>
</section>

</body>
</html>
```